Delvin & Associates - London New Letting and Property Management Company *

Delvin & Associates LTD is a new company based in London, and works with brand new residential property in the city centre.

We are aiming to have 1000 new properties a year.

We are looking for something modern and minimalistic :
Logo ,Monogram, Paper Head and Business Card.

Target Market(s)

Internation landlords

Industry/Entity Type

Real Estate

Logo Text

Delvin & Associates

Colors

Designer to choose colors to be used in the design.

Requirements
Nice to have
• A particular monogram with "DA"
Should not have
• Little House over the logo

```html
<!DOCTYPE html>
<html lang="en">
<head>
<meta charset="utf-8">
<title>Delvin &amp; Associates – Stationery</title>
<link rel="stylesheet" href="https://fonts.googleapis.com/css2?family=Old+Standard+TT:wght@400;700&display=swap">
<style>
  :root {
    --page-bg: #ffffff;
    --paper: #f2f2f4;
    --ink: #111111;
    --blue: #6f9bd1;
    --green: #86bb9a;
    --grey-dash: #d2d2d4;
  }
  * { margin: 0; padding: 0; box-sizing: border-box; }
  html, body { width: 1200px; height: 848px; overflow: hidden; background: var(--page-bg); }
  body { position: relative; font-family: "Old Standard TT", Georgia, serif; color: var(--ink); }

  .letterhead, .card, .dash, .wordmark, .company-line, .contact, .address, .person { position: absolute; }

  .dash { width: 19px; height: 7px; }
  .dash--blue { background: var(--blue); }
  .dash--green { background: var(--green); }
  .dash--grey { background: var(--grey-dash); }

  .letterhead { left: 263px; top: 49px; width: 510px; height: 721px; background: var(--paper); }

  .wordmark {
    left: 0; width: 100%; text-align: center;
    font-size: 22px; line-height: 1.15; color: var(--ink);
    display: flex; justify-content: center; align-items: center; gap: 8px;
  }
  .wordmark__square { width: 10px; height: 10px; background: var(--ink); flex: none; }

  .company-line {
    left: 0; width: 100%; text-align: center;
    font-size: 8.5px; letter-spacing: 0.3px; text-transform: uppercase;
  }

  .contact, .address { font-size: 8.5px; line-height: 11.5px; }
  .address { text-align: right; }

  .card { width: 318px; height: 199px; }
  .card--brand { left: 648px; top: 245px; background: var(--blue); }
  .card--person { left: 731px; top: 468px; background: var(--green); }

  .person { left: 0; width: 100%; text-align: center; }
  .person__name { font-size: 38px; line-height: 36px; color: var(--blue); }
  .person__role { font-size: 10px; margin-top: 6px; }
</style>
</head>
<body>

  <section class="letterhead">
    <span class="dash dash--blue" style="left:40px; top:39px;"></span>
    <span class="dash dash--green" style="left:433px; top:122px;"></span>
    <span class="dash dash--grey" style="left:328px; top:635px;"></span>

    <div class="wordmark" style="top:80px;"><span class="wordmark__square"></span>Delvin &amp; Associates</div>
    <p class="company-line" style="top:146px;">Delvin &amp; Associates LTD</p>

    <p class="contact" style="left:34px; top:655px;">+44 7000 218 604<br>hello@delvinassociates.co.uk<br>www.delvinassociates.co.uk</p>
    <p class="address" style="right:37px; top:655px;">42 Elm Row<br>LONDON<br>WF10 4AB</p>
  </section>

  <section class="card card--brand">
    <div class="wordmark" style="top:72px; font-size:24px;"><span class="wordmark__square"></span>Delvin &amp; Associates</div>
    <p class="company-line" style="top:162px; font-size:9.5px;">Delvin &amp; Associates LTD</p>
  </section>

  <section class="card card--person">
    <span class="dash dash--blue" style="left:258px; top:20px; height:6px;"></span>
    <span class="dash dash--blue" style="left:11px; top:88px; height:6px;"></span>
    <span class="dash dash--blue" style="left:187px; top:157px; height:6px;"></span>

    <div class="person" style="top:42px;">
      <h1 class="person__name" style="font-weight:400;">Owen<br>Hartley</h1>
      <p class="person__role">Real Estate Agent</p>
    </div>

    <p class="contact" style="left:17px; top:154px;">+44 7000 218 604<br>hello@delvinassociates.co.uk<br>www.delvinassociates.co.uk</p>
    <p class="address" style="right:21px; top:154px;">42 Elm Row<br>LONDON<br>WF10 4AB</p>
  </section>

</body>
</html>
```